Flyer-Design für Schwimmtraining für Triathleten
Zielgruppe
Angebot
Schwimmen: als Personal Training, in Kleingruppen oder im Kraulkurs
Schwimmen: Videoanalysen
Triathlon: Trainingspläne, Leistungsdiagnostik
Zielgruppe des Flyers:
Triathleten jeder Leistungsklasse
Flyer ist a) als Auslage in Sportgeschäften, b) als Beilage in Wettkampftüten von Triathlonwettkämpfen gedacht
Aufgabenstellung
Triathleten sind tendenziell technisch orientierte Menschen, vergleichsweise wohlhabend. Schwimmen ist häufig eher die verhasste aber notwendige Teil der drei Disziplinen.
Bitte kein Standardformat für den Flyer.
Die Herausforderung bei einem Flyer als Beigabe zum Wettkampfbeutel: Überlicherweise wird der ganze Packen Werbung achtlos weggeworfen. Design und Format sollen dazu beitragen, dass der Flyer heraussticht und möglichst beachtet wird.
Grundsätzliche Infos: www.flosswerk24.de

```html
<!DOCTYPE html>
<html lang="de">
<head>
<meta charset="utf-8">
<title>Flyer Schwimmtraining für Triathleten</title>
<link href="https://fonts.googleapis.com/css2?family=Archivo+Black&family=Work+Sans:wght@400;500;700;800&family=Oswald:wght@400;600&display=swap" rel="stylesheet">
<style>
:root{
  --black:#0b0b0b;
  --white:#ffffff;
  --yellow:#f9e51c;
  --grey:#8f9396;
  --stage:#e8e8e6;
  --skin-a:#e7b797;
  --skin-b:#b98468;
  --water-a:#7fa6ad;
  --water-b:#4e7b80;
  --lake-a:#a9cf7a;
  --lake-b:#5f8f6e;
}
*{margin:0;padding:0;box-sizing:border-box}
html,body{width:1200px;height:1200px;overflow:hidden;background:var(--stage)}
body{position:relative;font-family:"Work Sans",Arial,sans-serif}
.flyer{position:absolute;top:104px;width:448px;height:966px;overflow:hidden;box-shadow:0 4px 10px rgba(0,0,0,.25)}
.flyer--front{left:120px;background:var(--white)}
.flyer--back{left:637px;background:var(--white)}
.bg-shape{position:absolute;inset:0;width:100%;height:100%}
.headline{position:absolute;left:0;right:0;top:30px;font-family:"Archivo Black",Arial,sans-serif;font-size:48px;line-height:54px;text-align:center;letter-spacing:-.5px}
.headline .light{color:var(--white)}
.headline .accent{color:var(--yellow)}
.headline--back{color:var(--black);top:34px;font-size:40px}
.service{position:absolute;height:56px;padding-left:17px;display:flex;align-items:center;color:var(--white);font-weight:800;font-size:9px;line-height:11px;letter-spacing:.1px}
.service::before{content:"";position:absolute;left:0;top:0;width:11px;height:56px;border:4px solid var(--white);border-right:none}
.portrait{position:absolute;left:0;top:370px;width:212px;height:596px;border-radius:90px 90px 0 0;background:linear-gradient(180deg,var(--skin-a),var(--skin-b) 75%,#1c1c1e 76%)}
.badge{position:absolute;width:186px;height:186px;border-radius:50%;background:var(--yellow);display:flex;align-items:center;justify-content:center;font-family:"Oswald","Arial Narrow",sans-serif;text-align:center;overflow:hidden}
.badge__inner{transform:rotate(-9deg);line-height:1}
.badge__grey{color:var(--grey);font-weight:400;font-size:24px;display:block}
.badge__main{color:var(--black);font-weight:600;font-size:28px;display:block}
.badge__place{color:var(--black);font-family:"Work Sans",Arial,sans-serif;font-weight:700;font-size:8.5px;line-height:10px;display:block;margin-top:4px}
.flyer--front .badge{left:264px;top:340px}
.flyer--back .badge{left:263px;top:722px}
.quote{position:absolute;right:24px;top:546px;text-align:right;font-size:10px;line-height:18.3px;font-weight:500;color:var(--black)}
.quote b{font-weight:800}
.signature{position:absolute;left:228px;top:750px;width:170px;height:86px;background:linear-gradient(135deg,#f1f1f1,#e3e3e3)}
.contact{position:absolute;font-size:9px;line-height:12.5px;font-weight:500}
.flyer--front .contact{right:26px;top:848px;text-align:right;color:var(--black)}
.brand{position:absolute;font-family:"Work Sans",Arial,sans-serif;font-weight:800;font-size:23px;letter-spacing:-.5px}
.flyer--front .brand{right:26px;top:898px;color:var(--black)}
.flyer--back .brand{left:38px;top:892px;color:var(--white)}
.photo{position:absolute;inset:0}
.intro{position:absolute;left:38px;top:394px;width:390px;color:var(--white)}
.intro .intro__title{color:var(--yellow);font-weight:800;font-size:15px;line-height:24px;margin-bottom:8px}
.intro p{font-size:10.4px;line-height:18.3px;margin-bottom:6px}
.intro p b{font-weight:800}
.intro .intro__cta{color:var(--yellow);font-weight:800;font-size:15px;line-height:24.3px;margin-top:10px}
.address{position:absolute;left:38px;top:777px;color:var(--white);font-size:9.4px;line-height:12.5px;font-weight:500}
.address__name{font-weight:800;font-size:12px;line-height:15px}
.address__phone{position:absolute;left:38px;top:836px;color:var(--white);font-size:9px;line-height:12.5px;font-weight:500}
.social{position:absolute;left:236px;top:914px;display:flex;align-items:center;gap:7px;color:var(--yellow);font-size:13px;font-weight:500}
.social__dot{width:22px;height:22px;border-radius:50%;background:var(--yellow)}
.arrow{position:absolute;left:164px;top:766px}
</style>
</head>
<body>

<section class="flyer flyer--front">
  <svg class="bg-shape" viewBox="0 0 448 966" aria-hidden="true"><polygon points="0,0 448,0 448,435 0,495" fill="var(--black)"/></svg>
  <h1 class="headline"><span class="light">MAKE WATER</span><br><span class="accent">YOUR FRIEND</span></h1>

  <div class="service" style="left:242px;top:155px">ATHLETIK- UND<br>STABILISIERUNGSTRAINING<br>ALS PERSONAL TRAINING</div>
  <div class="service" style="left:81px;top:180px">TRAININGSPLÄNE &amp;<br>LEISTUNGSDIAGNOSTIK</div>
  <div class="service" style="left:33px;top:261px">SCHWIMMTRAINING –<br>ALS PERSONAL TRAINING IN KLEIN-<br>GRUPPEN ODER IM KRAULKURS</div>
  <div class="service" style="left:282px;top:261px">VIDEOANALYSE DEINER<br>SCHWIMMTECHNIK</div>
  <div class="service" style="left:152px;top:330px">SCHWIMMSEMINARE</div>

  <div class="portrait" role="img" aria-label="Foto des Trainers in Badehose mit verschränkten Armen"></div>

  <div class="badge"><div class="badge__inner">
    <span class="badge__grey">SCHWIMM-</span>
    <span class="badge__grey">TRAINING FÜR</span>
    <span class="badge__main">TRIATHLETEN</span>
    <span class="badge__place">IN MÜNCHEN, MALLORCA<br>UND LIECHTENSTEIN</span>
  </div></div>

  <p class="quote">„SERVUS UND EIN HERZLICHES<br>WILLKOMMEN BEI FLOSSWERK24, <b>DEINEM</b><br><b>PERSONAL TRAINER FÜR</b><br><b>SCHWIMMEN, TRIATHLON UND</b><br><b>AUSDAUERSPORT</b>. ICH BIETE DIR<br>SCHWIMMTECHNIK-TRAINING,<br>KRAULKURSE, TRAININGSPLÄNE<br>&amp; LEISTUNGSDIAGNOSTIK UND<br>SCHWIMMSEMINARE AN –<br>IN MÜNCHEN, MALLORCA UND<br>LIECHTENSTEIN.“</p>

  <div class="signature" role="img" aria-label="Handschriftliche Unterschrift Malte"></div>

  <p class="contact">Melde dich mobil (0176-48213309) oder<br>per E-Mail (malte@flosswerk24.de) bei mir!</p>
  <div class="brand">flosswerk24.de</div>
</section>

<section class="flyer flyer--back">
  <svg class="bg-shape" viewBox="0 0 448 966" aria-hidden="true"><polygon points="0,386 448,305 448,966 0,966" fill="var(--black)"/></svg>
  <h2 class="headline headline--back">BEAT THE BEAST</h2>

  <svg class="photo" viewBox="0 0 448 966">
    <defs>
      <linearGradient id="gWater" x1="0" y1="0" x2="0" y2="1"><stop offset="0" stop-color="var(--water-a)"/><stop offset="1" stop-color="var(--water-b)"/></linearGradient>
      <linearGradient id="gLake" x1="0" y1="0" x2="1" y2="1"><stop offset="0" stop-color="var(--lake-a)"/><stop offset="1" stop-color="var(--lake-b)"/></linearGradient>
    </defs>
    <polygon points="0,159 232,122 232,328 0,373" fill="url(#gWater)" role="img" aria-label="Foto: Triathlet mit gelber Badekappe steigt aus dem See"/>
    <polygon points="246,117 448,83 448,217 246,236" fill="url(#gWater)" role="img" aria-label="Foto: Schwimmer im offenen Wasser beim Kraulen"/>
    <polygon points="246,248 448,228 448,302 246,328" fill="url(#gLake)" role="img" aria-label="Foto: Schwimmer neben gelber Wendeboje"/>
  </svg>

  <div class="intro">
    <h3 class="intro__title">DU SUCHST EINEN KOMPETENTEN TRAINER<br>FÜR SCHWIMMEN ODER TRIATHLON?</h3>
    <p>Jemanden, der deine aktuellen Schwächen präzise analysiert,<br>ein genau auf dich und deine Kompetenzen zugeschnittenes<br>Personal Training entwirft und mit dir gemeinsam effizient und<br>fokussiert an deinen Zielen arbeitet?</p>
    <p>Mein Name ist <b>Malte Kessler</b> und dein Training bei mir profitiert<br>nicht nur von vier Jahrzehnten persönlicher Wettkampferfahrung im<br>Schwimm-, Triathlon- und Laufsport, sondern ebenso von meinen<br>vielfältigen Ausbildungen zum Trainer, Ernährungsberater und<br>systemischen Körpercoach.</p>
    <p class="intro__cta">LASS ES UNS GEMEINSAM ANGEHEN –<br>IM PERSONAL TRAINING, IN DER<br>KLEINGRUPPE ODER IN EINEM MEINER<br>KURSE ODER SEMINARE!</p>
  </div>

  <div class="address">
    <div class="address__name">MALTE KESSLER</div>
    Kastanienweg 14<br>81675 München
  </div>
  <svg class="arrow" width="72" height="26" viewBox="0 0 72 26" aria-hidden="true">
    <path d="M70 4 C50 8 30 14 6 18" stroke="var(--yellow)" stroke-width="4" fill="none" stroke-linecap="round"/>
    <path d="M16 8 L4 18 L18 23" stroke="var(--yellow)" stroke-width="4" fill="none" stroke-linecap="round" stroke-linejoin="round"/>
  </svg>
  <p class="address__phone">Melde dich mobil (0176-48213309) oder<br>per E-Mail (malte@flosswerk24.de) bei mir!</p>

  <div class="badge"><div class="badge__inner">
    <span class="badge__grey">SCHWIMM-</span>
    <span class="badge__grey">TRAINING FÜR</span>
    <span class="badge__main">TRIATHLETEN</span>
    <span class="badge__place">IN MÜNCHEN, MALLORCA<br>UND LIECHTENSTEIN</span>
  </div></div>

  <div class="brand">flosswerk24.de</div>
  <div class="social"><span class="social__dot"></span>@flosswerk24</div>
</section>

</body>
</html>
```